Birchmead Assurance Group Ltd needs a business card and logo

We need a logo for documents, invoices etc and a business card to match. We are a health auditing, training and consulting company based in NZ and working in both Australia and NZ. We ensure health organisations meet all their compliance requirements and develop expertise in the health auditing sector. The design should in some way reflect either symbols for quality management in the health sector.

Target Market(s)

Health providers and those wishing to increase their capability in meeting and understanding compliance requirements

Industry/Entity Type

Business

Contact Information for Business Card

Logo plus contact details

Logo Text

Health auditing, consultancy and training

Requirements
Must have
• Name and contact details director: Clara Hotham, chotham@bag-example.co.nz, PO Box 419, Totara Bay, NZ, cell +6427390516

```html
<!DOCTYPE html>
<html lang="en">
<head>
<meta charset="utf-8">
<title>Birchmead Assurance Group Ltd – Business Card</title>
<link href="https://fonts.googleapis.com/css2?family=Didact+Gothic&display=swap" rel="stylesheet">
<style>
  :root {
    --backdrop: #2b2b2b;
    --card: #fbfbfb;
    --ink: #1e1e1e;
    --ink-soft: #2e2e2e;
    --green-dark: #4f8f74;
    --green-light: #82b8a0;
  }
  * { margin: 0; padding: 0; box-sizing: border-box; }
  html, body {
    width: 1200px; height: 900px; overflow: hidden;
    background: var(--backdrop);
    font-family: "Didact Gothic", "Century Gothic", sans-serif;
  }
  .canvas {
    width: 1200px; height: 900px;
    display: flex; flex-direction: column;
    align-items: center; justify-content: center; gap: 48px;
  }
  .card {
    position: relative;
    width: 660px; height: 377px;
    background: var(--card);
    box-shadow: 0 8px 24px rgba(0,0,0,.45);
    overflow: hidden;
  }
  .brand {
    position: absolute;
    display: flex; align-items: center; gap: 14px;
    white-space: nowrap;
  }
  .brand-dot {
    width: 34px; height: 34px; border-radius: 50%;
    background: var(--green-dark); flex: none;
  }
  .brand-name {
    color: var(--ink-soft);
    font-size: 27px; line-height: 1.15; font-weight: 400;
  }
  .card-back .brand { left: 140px; top: 160px; }
  .top-band {
    position: absolute; top: 0; left: 0; right: 0; height: 12px;
    display: flex; gap: 4px;
  }
  .top-band .band-main { flex: 0 0 68%; background: var(--green-dark); }
  .top-band .band-end { flex: 1; background: var(--green-light); }
  .card-front .brand { left: 40px; top: 74px; }
  .contact {
    position: absolute; left: 370px; top: 190px;
    font-style: normal; white-space: nowrap;
    color: var(--ink); font-size: 15.5px; line-height: 1.45;
  }
  .contact-name {
    color: var(--green-dark); font-size: 17px; letter-spacing: .04em;
    margin-bottom: 10px;
  }
  .contact .label { color: var(--green-light); display: inline-block; width: 22px; }
</style>
</head>
<body>
<main class="canvas">
  <section class="card card-back" aria-label="Business card back">
    <div class="brand">
      <span class="brand-dot"></span>
      <span class="brand-name">Birchmead Assurance Group Ltd</span>
    </div>
  </section>

  <section class="card card-front" aria-label="Business card front">
    <div class="top-band"><span class="band-main"></span><span class="band-end"></span></div>
    <div class="brand">
      <span class="brand-dot"></span>
      <span class="brand-name">Birchmead Assurance Group Ltd</span>
    </div>
    <address class="contact">
      <p class="contact-name">CLARA HOTHAM</p>
      <p><span class="label">M:</span> +6427390516</p>
      <p><span class="label">E:</span> chotham@bag-example.co.nz</p>
      <p>PO Box 419, Totara Bay, NZ</p>
    </address>
  </section>
</main>
</body>
</html>
```